Lantern

My company name is lantern. The logo is attached. I am the business owner.
Name Gordon Pileck
Phone number- 2018347265
email- Gordon_pileck@mailbrook.net
Website is not live yet but it will be workwithlantern.com
the current beta link is- https://site.qvbtstage.com/lantern-v3/
on the back write “ find creative pros”
Use that beta link as reference for typography and colors on card.

```html
<!DOCTYPE html>
<html lang="en">
<head>
<meta charset="utf-8">
<title>Lantern Business Card</title>
<link href="https://fonts.googleapis.com/css2?family=Poppins:wght@400;500;600;700;800&display=swap" rel="stylesheet">
<style>
  :root {
    --stage: #1b1b1b;
    --card-back: #0f0f0f;
    --card-front: #1f1f1f;
    --ink-deep: #0b0b0b;
    --white: #f2f2f2;
    --soft-white: #d8d8d8;
    --accent: #d4552a;
    --rule: #8a8a8a;
  }
  * { box-sizing: border-box; margin: 0; padding: 0; }
  html, body {
    width: 1200px; height: 1200px; overflow: hidden;
    background: var(--stage);
    font-family: "Poppins", sans-serif;
  }
  .canvas {
    width: 1200px; height: 1200px;
    display: flex; flex-direction: column; align-items: center; justify-content: center;
    gap: 44px;
  }
  .card {
    position: relative;
    width: 900px; height: 514px;
    border-radius: 22px;
    overflow: hidden;
  }

  /* Back side */
  .card-back { background: var(--card-back); }
  .card-back .pattern-fill {
    position: absolute; inset: 0;
    background: linear-gradient(115deg, #0c0c0c 0%, #161616 45%, #262626 100%);
  }
  .tagline-block {
    position: absolute; left: 250px; top: 212px;
    display: flex; align-items: flex-start; gap: 18px;
  }
  .tagline-mark {
    width: 30px; height: 30px; margin-top: 10px;
    border: 3px solid var(--accent); border-radius: 50%;
    flex: none;
  }
  .tagline-title {
    color: var(--white); font-weight: 600; font-size: 44px; line-height: 1.1;
    letter-spacing: 0.5px;
  }
  .tagline-sub {
    color: var(--soft-white); font-weight: 400; font-size: 15px; margin-top: 6px;
    letter-spacing: 0.3px;
  }

  /* Front side */
  .card-front { background: var(--card-front); }
  .backdrop-word {
    position: absolute; left: -14px; top: -18px;
    font-weight: 800; font-size: 212px; line-height: 1;
    color: var(--ink-deep); letter-spacing: -6px; white-space: nowrap;
  }
  .brand-name {
    position: absolute; left: 70px; top: 186px;
    font-weight: 700; font-size: 62px; line-height: 1;
    color: var(--white); letter-spacing: -1px;
  }
  .divider {
    position: absolute; left: 0; right: 0; top: 268px;
    height: 1px; background: var(--rule);
  }
  .person {
    position: absolute; left: 70px; top: 290px;
  }
  .person-name {
    color: var(--white); font-weight: 600; font-size: 30px; letter-spacing: 0.5px;
  }
  .person-role {
    color: var(--accent); font-weight: 500; font-size: 22px; letter-spacing: 1px; margin-top: -4px;
  }
  .contact-list {
    position: absolute; left: 470px; top: 360px;
    list-style: none;
    display: flex; flex-direction: column; gap: 10px;
  }
  .contact-item {
    display: flex; align-items: center; gap: 16px;
    color: var(--white); font-size: 24px; font-weight: 400; letter-spacing: 0.4px;
  }
  .contact-icon { width: 24px; height: 24px; flex: none; }
</style>
</head>
<body>
  <main class="canvas">
    <section class="card card-back">
      <div class="pattern-fill" role="img" aria-label="Repeating tonal brand wordmark pattern in dark greys"></div>
      <div class="tagline-block">
        <span class="tagline-mark"></span>
        <div>
          <h2 class="tagline-title">Find creative pros</h2>
          <p class="tagline-sub">Work with local professionals.</p>
        </div>
      </div>
    </section>

    <section class="card card-front">
      <div class="backdrop-word" aria-hidden="true">LANTERN</div>
      <h1 class="brand-name">LANTERN</h1>
      <div class="divider"></div>
      <div class="person">
        <p class="person-name">GORDON PILECK</p>
        <p class="person-role">CREATOR</p>
      </div>
      <ul class="contact-list">
        <li class="contact-item">
          <svg class="contact-icon" viewBox="0 0 24 24" fill="none" stroke="#d4552a" stroke-width="2" stroke-linejoin="round">
            <path d="M5 3h4l2 5-2.5 1.5a11 11 0 0 0 6 6L16 13l5 2v4a2 2 0 0 1-2 2A16 16 0 0 1 3 5a2 2 0 0 1 2-2z"/>
          </svg>
          <span>2018347265</span>
        </li>
        <li class="contact-item">
          <svg class="contact-icon" viewBox="0 0 24 24">
            <rect x="2" y="5" width="20" height="14" rx="1" fill="#d4552a"/>
            <path d="M2.5 6l9.5 7 9.5-7" fill="none" stroke="#1f1f1f" stroke-width="1.6"/>
          </svg>
          <span>Gordon_pileck@mailbrook.net</span>
        </li>
        <li class="contact-item">
          <svg class="contact-icon" viewBox="0 0 24 24" fill="none" stroke="#d4552a" stroke-width="1.8">
            <circle cx="12" cy="12" r="10"/>
            <ellipse cx="12" cy="12" rx="4.5" ry="10"/>
            <path d="M2 12h20M4 7h16M4 17h16"/>
          </svg>
          <span>workwithlantern.com</span>
        </li>
      </ul>
    </section>
  </main>
</body>
</html>
```